Restoration Specialist in need of business card designs

One side of the business card is a bathroom ripped out down to the studs with just a sink and toilet and then the other side is the bathroom (same sink and toilet) but put back together. Like a before and after on each side behind our information. Stand out, hard to forget, business cards for my restoration company. I want a unique concept all together.
Must include in no particular order:
our business name "Brightwell Renovations"
Possible Logo for a restoration company
Owner; Dennis Holloway
410-867-3092
dholloway@brightwellrenovationsMD.com
BrightwellRenovationsMD.com (our company website) BUT I am open to any and all designs and options.

Target Market(s)

Customers, Men in the mitigation, plumbing, electrical, HVAC, Roofing, insurance companies

Industry/Entity Type

Restoration/ construction

Contact Information for Business Card

Must include in no particular order: our business name "Brightwell Renovations" Owner; Dennis Holloway 410-867-3092 dholloway@brightwellrenovationsMD.com BrightwellRenovationsMD.com (our company website) MAY include a list of our services: Residential~ Emergency Response ~ Board- up~ Complete Restoration

Font styles to use
Serif

Colors
0054AA
0677BA
7BADD7
CADEEF
E8F1F8
F0912C
F2A743
F7CA91
FBE8D2
FDF5EE

Requirements
Must have
• unique, memorable, not something men have seen over and over again,
Nice to have
• eye catching
Should not have
• Been something I could have made by myself

```html
<!DOCTYPE html>
<html lang="en">
<head>
<meta charset="utf-8">
<title>Brightwell Renovations – Business Card</title>
<link rel="stylesheet" href="https://fonts.googleapis.com/css2?family=Roboto+Slab:wght@400;700;800&family=Montserrat:wght@400;500;700&display=swap">
<style>
  :root {
    --stage: #2b2b2d;
    --navy: #15384f;
    --navy-ink: #17324a;
    --emboss: #0c2536;
    --orange: #f0822a;
    --paper: #ffffff;
    --rule: #1d3d57;
  }
  * { box-sizing: border-box; margin: 0; padding: 0; }
  html, body { width: 1200px; height: 875px; overflow: hidden; }
  body {
    background: var(--stage);
    display: flex;
    flex-direction: column;
    align-items: center;
    justify-content: center;
    gap: 40px;
  }
  .card {
    width: 660px;
    height: 377px;
    border-radius: 28px;
    position: relative;
    overflow: hidden;
    box-shadow: 0 14px 30px rgba(0,0,0,.45);
  }

  /* Front */
  .card-front {
    background: linear-gradient(100deg, #2a5570 0%, var(--navy) 22%, var(--navy) 100%);
    display: flex;
    flex-direction: column;
    align-items: center;
    justify-content: center;
    gap: 44px;
  }
  .front-brand {
    display: flex;
    align-items: center;
    gap: 16px;
  }
  .front-brand .mark {
    width: 26px; height: 26px;
    background: var(--emboss);
    flex: none;
  }
  .front-brand .name {
    font-family: "Roboto Slab", serif;
    font-weight: 800;
    font-size: 40px;
    line-height: 1.05;
    color: var(--emboss);
    text-transform: uppercase;
  }
  .services {
    font-family: "Montserrat", sans-serif;
    font-weight: 700;
    font-size: 16px;
    line-height: 1.3;
    color: var(--orange);
    text-align: center;
  }

  /* Back */
  .card-back {
    background: var(--paper);
    display: flex;
    align-items: center;
    justify-content: center;
    padding: 0 30px 30px;
  }
  .back-brand {
    flex: none;
    width: 205px;
    display: flex;
    align-items: flex-start;
    gap: 8px;
    align-self: center;
    margin-top: 50px;
  }
  .back-brand .mark {
    width: 12px; height: 12px;
    margin-top: 7px;
    background: var(--navy-ink);
    flex: none;
  }
  .back-brand .name {
    font-family: "Roboto Slab", serif;
    font-weight: 800;
    font-size: 23px;
    line-height: 1.1;
    color: var(--orange);
    text-transform: uppercase;
    white-space: nowrap;
  }
  .divider {
    flex: none;
    width: 2px;
    height: 132px;
    background: var(--rule);
    margin: 0 20px 0 10px;
  }
  .contact { flex: none; }
  .contact .person {
    font-family: "Roboto Slab", serif;
    font-weight: 700;
    font-size: 24px;
    color: var(--navy-ink);
    line-height: 1.1;
    white-space: nowrap;
  }
  .contact .role {
    font-family: "Montserrat", sans-serif;
    font-size: 12px;
    color: var(--navy-ink);
    margin-bottom: 12px;
  }
  .contact ul { list-style: none; }
  .contact li {
    display: flex;
    align-items: center;
    gap: 8px;
    font-family: "Montserrat", sans-serif;
    font-size: 12px;
    color: var(--navy-ink);
    line-height: 1.7;
    white-space: nowrap;
  }
  .contact svg { width: 12px; height: 12px; fill: var(--orange); flex: none; }
</style>
</head>
<body>

  <section class="card card-front" aria-label="Card front">
    <div class="front-brand">
      <span class="mark"></span>
      <span class="name">Brightwell<br>Renovations</span>
    </div>
    <p class="services">Residential~ Emergency Response ~ Board- up~ Storm<br>Protection~ Complete Restoration</p>
  </section>

  <section class="card card-back" aria-label="Card back">
    <div class="back-brand">
      <span class="mark"></span>
      <span class="name">Brightwell<br>Renovations</span>
    </div>
    <div class="divider"></div>
    <div class="contact">
      <p class="person">Dennis Holloway</p>
      <p class="role">Owner</p>
      <ul>
        <li>
          <svg viewBox="0 0 24 24"><path d="M6.6 10.8a15.1 15.1 0 0 0 6.6 6.6l2.2-2.2a1 1 0 0 1 1-.25 11.4 11.4 0 0 0 3.6.57 1 1 0 0 1 1 1V20a1 1 0 0 1-1 1A17 17 0 0 1 3 4a1 1 0 0 1 1-1h3.5a1 1 0 0 1 1 1c0 1.25.2 2.45.57 3.57a1 1 0 0 1-.25 1z"/></svg>
          410-867-3092
        </li>
        <li>
          <svg viewBox="0 0 24 24"><path d="M2 5h20v14H2z M2 5l10 8 10-8" fill="none" stroke="#f0822a" stroke-width="2.4"/></svg>
          dholloway@brightwellrenovationsMD.com
        </li>
        <li>
          <svg viewBox="0 0 24 24"><circle cx="12" cy="12" r="9" fill="none" stroke="#f0822a" stroke-width="2.4"/><path d="M3 12h18M12 3c3 3 3 15 0 18M12 3c-3 3-3 15 0 18" fill="none" stroke="#f0822a" stroke-width="1.8"/></svg>
          www.BrightwellRenovationsMD.com
        </li>
      </ul>
    </div>
  </section>

</body>
</html>
```